EPC Marketing Flyer Pinefold HC

Company Name: Pinefold Homecheck Ltd
Product: Residential EPCs
Territory: Nationwide (UK)
Marketing channel: Flyer will be used for email and postal mailshots. We have not targeted this particular segment of the market before, so we need it to be eye catching, clearly messaged and encourage the recipient to get in touch.

We need a flyer to promote our services to conduct EPCs owned by public and private sector for residential ONLY (NOT Commercial), on a large or small scale.

Our Surveyors: experienced and accredited surveyors, quality service, quick and professional

Our Business: Warm Ledger Accredited, Reputation in business for excellence, fast growing

Our Service: Friendly, high quality, quick and professional

Colours: Designs in green and white (same shade as corporate colours), with our logo, and warm ledger accreditation logo, promoting our business.

Target Market(s)

Estate Agencies, Housing Associations, Local Authorities (Housing Departments), House Builders (NOT Home Owners Directly)

Industry/Entity Type

It Company

Font styles to use
Sans Serif
Other font styles liked:
• Calibri

Colors
add136
9bcb3c
cadf82
f6faec
eaf2ce

Requirements
Must have
• Our contact number etc must be clearly visible, and that we do EPCs
• Must state: What is an EPC? An EPC (Energy Performance Certificate) gives a property an energy efficiency rating from A (most efficient) to G (least efficient) and is valid for 10 years. An EPC can also provide recommendations on home improvement measures which once complete can improve the energy efficiency of the property.
• Who needs and EPC? All landlords and home owners, as all properties available to buy or rent require a valid and current EPC.
• Contact details:
• Tel: 08000 915 462
• Website: www.pinefold-hc.co.uk
• Email: epc@pinefold-hc.co.uk
• we must also be ably to print out the flyer
Nice to have
• Nice images to accompany the text which give a feeling of Environmentally Green, Home Energy Efficiency, Home Warmth and family - see example attached. And image of survey professional at work.
Should not have
• Any reference to cost or pricing
• Warm ledger logo art work must not be any other size that that specified in guidance document attached.

```html
<!DOCTYPE html>
<html lang="en">
<head>
<meta charset="utf-8">
<title>Residential EPCs – Pinefold Homecheck Ltd</title>
<link rel="stylesheet" href="https://fonts.googleapis.com/css2?family=Arimo:wght@400;700&family=Open+Sans:wght@400;600&family=Roboto+Condensed:wght@700&display=swap">
<style>
  :root {
    --green-dark: #2f7d20;
    --green-mid: #3f9a2c;
    --green-head: #5c9a2e;
    --green-light: #9bcb3c;
    --green-pale: #cadf82;
    --green-wash: #eaf2ce;
    --green-mist: #f6faec;
    --text-body: #555a55;
    --text-dark: #222;
    --text-url: #3a3a3a;
    --rule: #9a9a9a;
    --white: #ffffff;
  }
  * { box-sizing: border-box; margin: 0; padding: 0; }
  html, body { width: 900px; height: 1200px; overflow: hidden; background: var(--white); }
  .flyer {
    position: relative;
    width: 900px;
    height: 1200px;
    overflow: hidden;
    background: linear-gradient(to bottom, var(--white) 0%, var(--white) 42%, var(--green-mist) 60%, var(--green-wash) 100%);
    font-family: "Open Sans", sans-serif;
  }
  .hero { position: absolute; left: 0; top: 0; width: 900px; height: 470px; }
  .territory {
    position: absolute; left: 502px; top: 28px;
    font-family: "Arimo", sans-serif; font-weight: 700; font-size: 26px; color: var(--text-dark);
  }
  .badge { position: absolute; left: 648px; top: 284px; width: 200px; height: 200px; }
  .brand {
    position: absolute; left: 40px; top: 482px;
    width: 390px;
    display: flex; align-items: center; gap: 14px;
  }
  .brand-dot { width: 46px; height: 46px; border-radius: 50%; background: var(--green-light); flex: none; }
  .brand-name {
    width: 300px;
    font-family: "Arimo", sans-serif; font-weight: 700; font-size: 28px; line-height: 1.15; color: var(--green-mid);
  }
  .contact { position: absolute; left: 465px; top: 490px; width: 410px; font-family: "Arimo", sans-serif; font-weight: 700; }
  .contact-web { font-size: 33px; color: var(--text-url); letter-spacing: -0.3px; white-space: nowrap; }
  .contact-mail { font-size: 22px; color: var(--text-dark); margin-top: 12px; white-space: nowrap; }
  .divider { position: absolute; left: 420px; top: 646px; width: 1px; height: 475px; background: var(--rule); }
  .col { position: absolute; top: 640px; }
  .col-left { left: 55px; width: 330px; }
  .col-right { left: 457px; width: 385px; }
  .title {
    font-family: "Arimo", sans-serif; font-weight: 700; font-size: 40px; color: var(--green-dark);
    letter-spacing: -0.5px; line-height: 1.1;
  }
  .subtitle {
    font-family: "Arimo", sans-serif; font-weight: 700; font-size: 31px; color: var(--green-head);
    margin-top: 34px; line-height: 1.1;
  }
  .body {
    font-size: 14.5px; line-height: 22.5px; color: var(--text-body); text-align: justify;
  }
  .col-left .body { margin-top: 14px; }
  .col-right .body { margin-top: 14px; }
  .col-right .body + .body { margin-top: 13px; }
  .features { list-style: none; margin-top: 30px; }
  .features li {
    display: flex; align-items: center; gap: 12px;
    font-family: "Open Sans", sans-serif; font-weight: 600; font-size: 19.5px; color: var(--text-dark);
    height: 29px;
  }
  .features li::before {
    content: ""; width: 10px; height: 10px; border-radius: 50%;
    border: 4px solid #4a4a4a; background: var(--white); flex: none;
  }
  .who {
    font-family: "Arimo", sans-serif; font-weight: 700; font-size: 25px; color: var(--green-head);
    margin-top: 50px;
  }
  .who-body { font-size: 14.5px; line-height: 22px; color: var(--text-body); margin-top: 12px; width: 320px; }
  .cta {
    position: absolute; left: 0; bottom: 0; width: 900px; height: 60px;
    background: var(--green-mid);
    display: flex; align-items: center; justify-content: center; gap: 8px;
    font-family: "Roboto Condensed", sans-serif; font-weight: 700; color: var(--white);
  }
  .cta-label { font-size: 28px; }
  .cta-number { font-size: 35px; letter-spacing: 0.5px; }
</style>
</head>
<body>
<main class="flyer">
  <svg class="hero" viewBox="0 0 900 470">
    <defs>
      <linearGradient id="heroPhoto" x1="0" y1="0" x2="1" y2="1">
        <stop offset="0" stop-color="#a9c96a"/>
        <stop offset="0.45" stop-color="#cfe0a0"/>
        <stop offset="1" stop-color="#e9efd8"/>
      </linearGradient>
      <linearGradient id="bandDark" x1="0" y1="0" x2="1" y2="0">
        <stop offset="0" stop-color="#2f7d20"/>
        <stop offset="0.6" stop-color="#3f9a2c"/>
        <stop offset="1" stop-color="#2f7d20"/>
      </linearGradient>
    </defs>
    <path d="M0 0 H820 C860 120 845 280 700 360 C520 432 220 420 0 365 Z"
          fill="url(#heroPhoto)" role="img"
          aria-label="Photo: hands cupping a small green grass-covered house model against a soft green background"/>
    <path d="M820 0 H850 C885 130 870 300 720 385 C540 462 220 448 0 388 V365 C220 420 520 432 700 360 C845 280 860 120 820 0 Z"
          fill="url(#bandDark)"/>
    <path d="M850 0 H870 C900 140 885 310 735 396 C560 472 240 458 0 408 V388 C220 448 540 462 720 385 C870 300 885 130 850 0 Z"
          fill="var(--green-light)" opacity="0.85"/>
    <path d="M870 0 H900 V120 C895 250 860 330 760 400 C860 320 895 200 870 0 Z"
          fill="var(--green-pale)"/>
  </svg>

  <div class="territory">Nationwide (UK)</div>

  <svg class="badge" viewBox="0 0 200 200" role="img" aria-label="Warm Ledger approved provider badge">
    <circle cx="100" cy="100" r="96" fill="#d9d9d9"/>
    <circle cx="100" cy="100" r="86" fill="#f2f2f2" stroke="#bdbdbd" stroke-width="2"/>
  </svg>

  <div class="brand">
    <span class="brand-dot"></span>
    <span class="brand-name">Pinefold Homecheck Ltd</span>
  </div>

  <div class="contact">
    <div class="contact-web">www.pinefold-hc.co.uk</div>
    <div class="contact-mail">Email: epc@pinefold-hc.co.uk</div>
  </div>

  <div class="divider"></div>

  <section class="col col-left">
    <h1 class="title">Residential EPCs</h1>
    <h2 class="subtitle">What is an EPC?</h2>
    <p class="body">An EPC (Energy Performance Certificate) gives a property an energy efficiency rating from A (most efficient) to G (least efficient) and is valid for 10 years. An EPC can also provide recommendations on home improvement measures which once complete can improve the energy efficiency of the property.</p>
    <ul class="features">
      <li>Free Loft and Cavity Insulation</li>
      <li>Energy Reduction</li>
      <li>Carbon Emission Reduction</li>
      <li>Energy Saving Tips</li>
      <li>Making Homes Warmer</li>
    </ul>
  </section>

  <section class="col col-right">
    <h2 class="title">What we do</h2>
    <p class="body">PHC focus is on meeting the demand for householders to achieve energy efficient upgrades to their homes in line with government targets and financial incentives.</p>
    <p class="body">Each of our team of field operators is trained and accredited to the highest standards in home surveying. Our mission is to work with carefully selected installers providing a high end finished product for our clients.</p>
    <p class="body">At PHC our personal but professional approach offers householders detailed advice on energy reduction, tariff optimisation and finance.</p>
    <h3 class="who">Who needs and EPC?</h3>
    <p class="who-body">All landlords and home owners, as all properties available to buy or rent require a valid and current EPC.</p>
  </section>

  <footer class="cta">
    <span class="cta-label">Call us today:</span>
    <span class="cta-number">08000 915 462</span>
  </footer>
</main>
</body>
</html>
```